Interior Stylist business card design needed

I need a business card for my new company in Sydney called "Pip Dunstane Designs". The business offers an interior styling and colour consultancy. My clients are generally not very design savvy (hence why they use me) and can range from being quite conservative to really wanting something "out there". They can be looking for a budget makeover or something more expensive / substantial. I'd like my business card design to be stylish (but not overly formal). I certainly don't want it to be conservative. I'd like it to stand out a bit! I don't really have any aversion to particular colours and I don't have a logo as such - my business name is really all I have.

Target Market(s)

As above - home owners, ranging from conservative to modern

Industry/Entity Type

Conservative

Contact Information for Business Card

Pip Dunstane Designs
Colour consultancy and interior styling
ph: 0417 382 605
email: pipdunstane@harvolink.net.au

Requirements
Should not have
• Old fashioned writing or motifs. No Times Roman font!!

```html
<!DOCTYPE html>
<html lang="en">
<head>
<meta charset="utf-8">
<title>Pip Dunstane Designs — Business Card</title>
<link rel="stylesheet" href="https://fonts.googleapis.com/css2?family=Pinyon+Script&family=Cormorant+SC:wght@500&family=Cormorant+Garamond:ital,wght@1,500&display=swap">
<style>
  :root {
    --stage: #2a2420;
    --olive-light: #4a4b38;
    --olive-dark: #2f3025;
    --band: #000000;
    --ink: #f2f0ea;
    --ink-soft: #d9d7cf;
  }
  * { box-sizing: border-box; margin: 0; padding: 0; }
  html, body {
    width: 1200px;
    height: 900px;
    overflow: hidden;
    background: var(--stage);
  }
  .stage {
    position: relative;
    width: 1200px;
    height: 900px;
  }
  .card {
    position: absolute;
    left: 300px;
    width: 600px;
    height: 343px;
    border-radius: 22px;
    overflow: hidden;
    box-shadow: 0 10px 28px rgba(0,0,0,0.55);
  }
  .card--front { top: 70px; }
  .card--back { top: 480px; }
  .card__pattern {
    position: absolute;
    inset: 0;
    background: radial-gradient(ellipse at 40% 35%, var(--olive-light), var(--olive-dark) 80%);
  }
  .band {
    position: absolute;
    background: var(--band);
    color: var(--ink);
  }
  .wordmark {
    display: flex;
    flex-direction: column;
    align-items: flex-end;
    line-height: 1;
  }
  .wordmark__name {
    font-family: "Pinyon Script", cursive;
    font-weight: 400;
    color: var(--ink);
  }
  .wordmark__sub {
    font-family: "Cormorant SC", serif;
    font-weight: 500;
    letter-spacing: 0.12em;
    color: var(--ink);
  }
  /* Front */
  .card--front .band--name {
    left: 0;
    top: 178px;
    width: 340px;
    height: 102px;
    display: flex;
    align-items: center;
    justify-content: flex-end;
    padding-right: 26px;
  }
  .card--front .wordmark__name { font-size: 42px; }
  .card--front .wordmark__sub { font-size: 17px; margin-top: -6px; }
  /* Back */
  .card--back .band--name {
    left: 222px;
    top: 42px;
    width: 200px;
    height: 78px;
    display: flex;
    align-items: center;
    justify-content: center;
  }
  .card--back .wordmark__name { font-size: 29px; }
  .card--back .wordmark__sub { font-size: 13px; margin-top: -4px; }
  .card--back .band--details {
    left: 180px;
    top: 148px;
    width: 376px;
    height: 195px;
    padding: 26px 0 0 34px;
    font-family: "Cormorant Garamond", serif;
    font-style: italic;
    font-weight: 500;
  }
  .tagline {
    font-size: 21px;
    letter-spacing: 0.02em;
    color: var(--ink);
  }
  .contact {
    list-style: none;
    margin: 26px 0 0 74px;
    font-size: 20px;
    color: var(--ink-soft);
  }
  .contact__item {
    display: flex;
    align-items: center;
    gap: 14px;
    margin-bottom: 10px;
  }
  .contact__icon {
    width: 16px;
    height: 16px;
    flex: none;
  }
</style>
</head>
<body>
<main class="stage">
  <section class="card card--front" aria-label="Business card front">
    <div class="card__pattern" role="img" aria-label="Olive green floral damask pattern background"></div>
    <div class="band band--name">
      <div class="wordmark">
        <span class="wordmark__name">Pip Dunstane</span>
        <span class="wordmark__sub">Designs</span>
      </div>
    </div>
  </section>

  <section class="card card--back" aria-label="Business card back">
    <div class="card__pattern" role="img" aria-label="Olive green floral damask pattern background"></div>
    <div class="band band--name">
      <div class="wordmark">
        <span class="wordmark__name">Pip Dunstane</span>
        <span class="wordmark__sub">Designs</span>
      </div>
    </div>
    <div class="band band--details">
      <p class="tagline">Colour consultancy and interior styling</p>
      <ul class="contact">
        <li class="contact__item">
          <svg class="contact__icon" viewBox="0 0 16 16" aria-hidden="true">
            <circle cx="8" cy="8" r="7" fill="none" stroke="currentColor" stroke-width="1"/>
            <path d="M5.6 4.6l1.2-.3.8 1.8-.8.6c.4.9 1 1.6 1.9 2l.6-.8 1.8.8-.3 1.2c-2.8.2-5.4-2.5-5.2-5.3z" fill="currentColor"/>
          </svg>
          <span>0417 382 605</span>
        </li>
        <li class="contact__item">
          <span class="contact__icon" aria-hidden="true" style="font-size:18px;line-height:16px;">@</span>
          <span>pipdunstane@harvolink.net.au</span>
        </li>
      </ul>
    </div>
  </section>
</main>
</body>
</html>
```